The homepage of a website

This is a simple project that should take from you a few minutes as what is needed is the design of the homepage only, the details are in the attached zip file

Please note that KLVTA board required a special tailored design where they got some parts from the different posted designs, if you are interested please follow the instructions in the below URL and submit your new updated designs as per the instructions (P.S. I will mark the project as guaranteed as an assurance to all of you)

http://qorvinworks.example/Projects/KLVTA/Design.jpg
Updates

Please note that KLVTA board required a special tailored design where they got some parts from the different posted designs, if you are interested please follow the instructions in the below URL and submit your new updated designs as per the instructions (P.S. I will mark the project as guaranteed as an assurance to all of you) http://qorvinworks.example/Projects/KLVTA/Design.jpg

```html
<!DOCTYPE html>
<html lang="en">
<head>
<meta charset="utf-8">
<title>Kelvra — Homepage</title>
<link rel="stylesheet" href="https://fonts.googleapis.com/css2?family=Arimo:ital,wght@0,400;0,700;1,400&family=Source+Sans+3:wght@300;400;600&display=swap">
<style>
  :root {
    --page-bg: #eceeef;
    --surface: #ffffff;
    --surface-soft: #fafafa;
    --ink: #1b2432;
    --ink-muted: #7a7f88;
    --ink-soft: #9a9ea5;
    --line: #eceef0;
    --dot: #dde1e6;
    --ring: #b8c2cc;
    --accent: #12bde6;
    --tag-bg: #e3e6ea;
    --tag-ink: #3a4350;
    --footer-bg: #1a2535;
    --footer-title: #2b5b8c;
    --footer-sub: #c7a283;
    --swatch-1: #04c4e8;
    --swatch-2: #584a5f;
    --swatch-3: #14001b;
    --swatch-4: #1eb3a1;
    --sans: "Arimo", Helvetica, Arial, sans-serif;
    --body: "Source Sans 3", "Myriad Pro", Arial, sans-serif;
  }
  * { box-sizing: border-box; margin: 0; padding: 0; }
  html, body { width: 1200px; height: 816px; overflow: hidden; }
  body { background: var(--page-bg); position: relative; font-family: var(--sans); color: var(--ink); }

  .page { position: absolute; left: 180px; top: 0; width: 840px; height: 816px; background: var(--surface); }
  .abs { position: absolute; }

  .slider-arrow { position: absolute; top: -14px; width: 36px; height: 36px; border-radius: 50%; background: var(--surface); }
  .slider-arrow svg { position: absolute; top: 14px; }
  .slider-arrow--prev { left: 162px; }
  .slider-arrow--prev svg { left: 12px; }
  .slider-arrow--next { left: 1003px; }
  .slider-arrow--next svg { left: 14px; }

  .feature { position: absolute; top: 0; width: 164px; text-align: center; }
  .feature__swatch { height: 47px; }
  .feature__text { margin-right: 10px; }
  .feature__title { margin-top: 16px; font-family: var(--body); font-size: 12px; color: var(--ink); line-height: 14px; }
  .feature__sub { margin-top: 3px; font-family: var(--body); font-size: 10px; color: var(--ink-soft); line-height: 12px; }

  .btn { position: absolute; height: 30px; line-height: 30px; border-radius: 3px; background: var(--ink); color: #fff; font-family: var(--sans); font-weight: 700; font-size: 10.5px; text-align: center; white-space: nowrap; }

  .divider { position: absolute; left: 180px; width: 840px; height: 1px; background: var(--line); }

  .testimonials__title { left: 180px; width: 840px; top: 210px; text-align: center; font-size: 20.5px; font-weight: 700; letter-spacing: -0.3px; }
  .testimonials__quote { left: 290px; width: 620px; top: 254px; text-align: center; font-size: 12.5px; line-height: 20px; color: var(--ink-muted); }
  .testimonials__source { left: 180px; width: 840px; top: 311px; text-align: center; font-size: 9.5px; font-weight: 700; color: var(--ink-muted); }
  .pager-dot { position: absolute; top: 353px; width: 16px; height: 16px; border-radius: 50%; background: var(--dot); }

  .widgets { position: absolute; left: 180px; top: 418px; width: 840px; height: 231px; background: var(--surface-soft); }
  .widget__title { position: absolute; top: 449px; font-size: 15px; font-weight: 700; }
  .widget__title--light { font-family: var(--body); font-weight: 400; font-size: 15.5px; }
  .widget__text { position: absolute; font-family: var(--body); font-size: 10px; line-height: 20.5px; color: var(--ink-muted); width: 218px; }
  .tweet { position: absolute; font-size: 10px; line-height: 17px; color: var(--ink-muted); width: 230px; }
  .tweet b { color: var(--ink); }
  .tweet em { font-style: italic; }

  .tag { position: absolute; height: 18px; line-height: 18px; background: var(--tag-bg); color: var(--tag-ink); font-size: 9.5px; font-weight: 700; padding: 0 8px 0 19px; white-space: nowrap;
         clip-path: polygon(8px 0, 100% 0, 100% 100%, 8px 100%, 0 50%); }
  .tag::before { content: ""; position: absolute; left: 8px; top: 7px; width: 4px; height: 4px; border-radius: 50%; background: var(--surface-soft); }

  .search { position: absolute; left: 746px; top: 576px; width: 223px; height: 30px; border: 1px solid #dfe2e6; border-radius: 3px; background: #fff; font-size: 10px; color: var(--ink-muted); line-height: 28px; padding-left: 9px; }

  .footer { position: absolute; left: 180px; top: 649px; width: 840px; height: 167px; background: var(--footer-bg); }
  .to-top { position: absolute; left: 583px; top: 636px; width: 35px; height: 35px; border-radius: 50%; background: var(--footer-bg); }
  .to-top svg { position: absolute; left: 12px; top: 9px; }
  .footer__title { left: 232px; top: 701px; font-family: var(--body); font-weight: 400; font-size: 40px; color: var(--footer-title); letter-spacing: 2px; line-height: 46px; }
  .footer__sub { left: 232px; top: 752px; font-family: var(--body); font-size: 10.5px; color: var(--footer-sub); line-height: 12px; letter-spacing: 0.35px; }
</style>
</head>
<body>
  <div class="page"></div>

  <div class="slider-arrow slider-arrow--prev"><svg width="10" height="12" viewBox="0 0 10 12"><path d="M7 1 2 6l5 5" fill="none" stroke="#b8bec6" stroke-width="2.4"/></svg></div>
  <div class="slider-arrow slider-arrow--next"><svg width="10" height="12" viewBox="0 0 10 12"><path d="M3 1l5 5-5 5" fill="none" stroke="#b8bec6" stroke-width="2.4"/></svg></div>

  <section class="features">
    <div class="feature" style="left:232px"><div class="feature__swatch" style="background:var(--swatch-1)"></div><div class="feature__text"><p class="feature__title">Text one</p><p class="feature__sub">Text one</p></div></div>
    <div class="feature" style="left:422px"><div class="feature__swatch" style="background:var(--swatch-2)"></div><div class="feature__text"><p class="feature__title">Text Two</p><p class="feature__sub">Text two</p></div></div>
    <div class="feature" style="left:612px"><div class="feature__swatch" style="background:var(--swatch-3)"></div><div class="feature__text"><p class="feature__title">Text Three</p><p class="feature__sub">text three</p></div></div>
    <div class="feature" style="left:804px"><div class="feature__swatch" style="background:var(--swatch-4)"></div><div class="feature__text"><p class="feature__title">Text four</p><p class="feature__sub">text four</p></div></div>
    <a class="btn" style="left:547px;top:116px;width:107px">Wanna read more?</a>
  </section>

  <div class="divider" style="top:180px"></div>

  <section class="testimonials">
    <h2 class="abs testimonials__title">What the Clients say!</h2>
    <p class="abs testimonials__quote">„Lorem ipsum dolor sit amet, consetetur sadipscing elitr, sed diam nonumy eirmod tempor invidunt ut labore et dolore magna aliquyam erat, sed diam voluptua.“</p>
    <p class="abs testimonials__source">Nortwell via Marketfold</p>
    <span class="pager-dot" style="left:502px"></span>
    <span class="pager-dot" style="left:528px"></span>
    <span class="pager-dot" style="left:554px"></span>
    <svg class="abs" style="left:580px;top:341px" width="40" height="40" viewBox="0 0 40 40">
      <circle cx="20" cy="20" r="18" fill="none" stroke="var(--ring)" stroke-width="2.5"/>
      <path d="M20 2 A18 18 0 0 1 38 20" fill="none" stroke="var(--accent)" stroke-width="2.5"/>
    </svg>
    <span class="pager-dot" style="left:630px"></span>
    <span class="pager-dot" style="left:656px"></span>
    <span class="pager-dot" style="left:682px"></span>
  </section>

  <div class="divider" style="top:417px"></div>
  <section class="widgets"></section>

  <h3 class="widget__title widget__title--light" style="left:232px">About Kelvra</h3>
  <p class="widget__text" style="left:232px;top:475px">Lorem ipsum dolor sit amet, consetetur sadipscing elitr, sed diam nonumy eirmod tempor invidunt ut labore et dolore magna aliquyam erat, sed diam voluptua.</p>
  <a class="btn" style="left:232px;top:576px;width:74px">More Infos</a>

  <h3 class="widget__title" style="left:489px">Chirply Widget</h3>
  <p class="tweet" style="left:489px;top:476px"><b>@Arlo</b> Lorem ipsum dolor sit amet, consetetur sadipscing elitr, sed. <em>1 day ago</em></p>
  <p class="tweet" style="left:489px;top:522px"><b>@Wendel K.</b> Lorem ipsum dolor sit amet, conse-tetur sadipscing elitr, sed. <em>2 day ago</em></p>
  <a class="btn" style="left:489px;top:576px;width:102px">Follow on Chirply</a>

  <h3 class="widget__title" style="left:746px">Tags Widget</h3>
  <span class="tag" style="left:746px;top:479px">webdesign</span>
  <span class="tag" style="left:838px;top:479px">tutorials</span>
  <span class="tag" style="left:746px;top:507px">icons</span>
  <span class="tag" style="left:812px;top:507px">layout</span>
  <span class="tag" style="left:877px;top:507px">textures</span>
  <span class="tag" style="left:746px;top:535px">buttons</span>
  <span class="tag" style="left:823px;top:535px">logos</span>
  <div class="search">Search and enter!</div>

  <footer class="footer"></footer>
  <div class="to-top"><svg width="11" height="8" viewBox="0 0 11 8"><path d="M1 7l4.5-4.5L10 7" fill="none" stroke="#fff" stroke-width="2.6"/></svg></div>
  <p class="abs footer__title">XXXXXXXXXX</p>
  <p class="abs footer__sub">XXXXXXXXXXXXXXXXXXXXXXXXXXXXXXXXXXXXXXXXX</p>
</body>
</html>
```